Tech Startup wants A4 and A3 Poster

We need an A4 and an A3 Poster for a new company in Australia called 'tolmu'. tolmu has created a personal safety app that records videos that are synchronised with the cloud. It also integrates your location. We want to have posters for the purpose of advertising. We would prefer if you looked at our website www.tolmu-example.com and even download the Orbix app at https://apps.example-store.net/details?id=com.orvex.tolmu and kept the theme we have used. The Poster should communicate in very terms what our product does with a focus on people downloading the app. Please find our logo attached.

Industry/Entity Type

Safety

```html
<!DOCTYPE html>
<html lang="en">
<head>
<meta charset="utf-8">
<title>tolmu – personal safety app poster</title>
<link rel="stylesheet" href="https://fonts.googleapis.com/css2?family=Fira+Sans+Condensed:wght@300;400;600;700&display=swap">
<style>
  :root {
    --brand-blue: #4a8dcd;
    --white: #ffffff;
    --photo-dark: #2a2a2e;
    --photo-warm: #8a5a48;
    --photo-light: #dfe7ee;
  }
  * { margin: 0; padding: 0; box-sizing: border-box; }
  html, body { width: 848px; height: 1200px; overflow: hidden; }
  body {
    background: var(--brand-blue);
    color: var(--white);
    font-family: "Fira Sans Condensed", "Arial Narrow", sans-serif;
  }
  .poster { position: relative; width: 848px; height: 1200px; overflow: hidden; background: var(--brand-blue); }

  .brand-mark {
    position: absolute; left: 18px; top: 8px;
    width: 262px; height: 262px; border-radius: 50%;
    background: var(--white);
  }
  .brand-name {
    position: absolute; left: 352px; top: 86px;
    font-weight: 300; font-size: 118px; line-height: 1; letter-spacing: 1px;
  }
  .tagline {
    position: absolute; left: 285px; top: 246px; width: 546px;
    font-weight: 400; font-size: 27.5px; line-height: 36px; text-align: justify;
  }
  .how-title {
    position: absolute; left: 14px; top: 362px;
    font-weight: 700; font-size: 41px; line-height: 1;
  }
  .how-text {
    position: absolute; left: 14px; top: 410px; width: 822px;
    font-weight: 400; font-size: 20.5px; line-height: 31px;
  }

  .app-photo { position: absolute; left: 0; top: 0; width: 848px; height: 1200px; }

  .feature { position: absolute; left: 469px; width: 362px; }
  .feature-head { position: relative; height: 48px; }
  .feature-icon { position: absolute; left: 10px; top: 0; }
  .feature-title {
    position: absolute; left: 96px; top: 10px;
    font-weight: 600; font-size: 25px; line-height: 1;
  }
  .feature-text {
    margin-top: 22px;
    font-weight: 300; font-size: 16.5px; line-height: 26.5px; text-align: justify;
  }
  .feature--video { top: 510px; }
  .feature--location { top: 730px; }
  .feature--cloud { top: 925px; }
  .feature--cloud .feature-title { left: 108px; }

  .availability {
    position: absolute; left: 482px; top: 1140px;
    display: flex; align-items: center; gap: 12px;
    font-weight: 400; font-size: 26px; line-height: 1;
  }
  .store-dot { width: 24px; height: 24px; border-radius: 50%; background: var(--white); }
</style>
</head>
<body>
<main class="poster">

  <div class="brand-mark" aria-hidden="true"></div>
  <h1 class="brand-name">tolmu</h1>

  <p class="tagline">Have you ever felt unsafe, threatened, or been bullied? Maybe you simply want a better way to create, manage, and store your video content?</p>

  <h2 class="how-title">How does it work?</h2>
  <p class="how-text">tolmu is a personal safety app that creates a video, combines it with your location, and uploads it to the cloud where we lock it for 10 days so that it cannot be deleted by anyone.</p>

  <svg class="app-photo" viewBox="0 0 848 1200" role="img" aria-label="Smartphone showing the app: a young woman wearing headphones on a city street at night, above an emergency contacts list">
    <defs>
      <linearGradient id="photoTone" x1="0" y1="0" x2="0" y2="1">
        <stop offset="0" stop-color="var(--photo-dark)"/>
        <stop offset="0.45" stop-color="var(--photo-warm)"/>
        <stop offset="0.78" stop-color="var(--photo-light)"/>
        <stop offset="1" stop-color="var(--white)"/>
      </linearGradient>
    </defs>
    <path d="M0 510 C120 500 250 540 330 610 C420 690 455 800 440 900 C425 1010 360 1110 265 1200 L0 1200 Z" fill="url(#photoTone)"/>
  </svg>

  <section class="feature feature--video">
    <div class="feature-head">
      <svg class="feature-icon" width="44" height="44" viewBox="0 0 44 44" fill="none" stroke="#fff" stroke-width="1.6" aria-hidden="true">
        <rect x="2" y="2" width="40" height="40"/>
        <line x1="11" y1="2" x2="11" y2="42"/><line x1="33" y1="2" x2="33" y2="42"/>
        <line x1="2" y1="12" x2="11" y2="12"/><line x1="2" y1="22" x2="11" y2="22"/><line x1="2" y1="32" x2="11" y2="32"/>
        <line x1="33" y1="12" x2="42" y2="12"/><line x1="33" y1="22" x2="42" y2="22"/><line x1="33" y1="32" x2="42" y2="32"/>
      </svg>
      <h3 class="feature-title">Video Recording</h3>
    </div>
    <p class="feature-text">Easily record videos in the background, even when the app is minimized. You can continue to use other apps at the same time that you are recording video. You can even have the screen turned off.</p>
  </section>

  <section class="feature feature--location">
    <div class="feature-head">
      <svg class="feature-icon" width="40" height="50" viewBox="0 0 40 50" fill="none" stroke="#fff" stroke-width="1.8" aria-hidden="true">
        <path d="M20 48 C10 34 3 26 3 18 A17 17 0 0 1 37 18 C37 26 30 34 20 48 Z"/>
        <circle cx="20" cy="18" r="7"/>
      </svg>
      <h3 class="feature-title">Location History</h3>
    </div>
    <p class="feature-text">Get instant access to your videos and generate video reports. You can access your content within the app or from your tablet or PC. Easily share videos with friends, family, or authorities.</p>
  </section>

  <section class="feature feature--cloud">
    <div class="feature-head">
      <svg class="feature-icon" width="54" height="40" viewBox="0 0 54 40" fill="none" stroke="#fff" stroke-width="1.6" aria-hidden="true">
        <path d="M12 36 H44 A8 8 0 0 0 44 20 A12 12 0 0 0 22 12 A10 10 0 0 0 8 22 A7 7 0 0 0 12 36 Z"/>
      </svg>
      <h3 class="feature-title">Sync to Cloud</h3>
    </div>
    <p class="feature-text">All your content is synced to our private servers to ensure the safe keeping of your content in an emergency. Files that are uploaded cannot be deleted for 10 days to ensure the integrity of your videos.</p>
  </section>

  <p class="availability">Now available on: <span class="store-dot" aria-hidden="true"></span><span>Orbix</span></p>

</main>
</body>
</html>
```